Dalton & Vesh Periodontics and Implant Solutions Business Card

We are a specialty dental practice- implants and periodontal surgery. We have just re-designed our logo and are building a new office and would like to re-design our business card. We are looking for something professional with a creative and artsy twist- something to stand out among the rest! Happy Designing!

I have uploaded all versions of our new logo and our current business card. We have 3 locations and 2 doctors.
Updates

Target Market(s)

55+

Industry/Entity Type

Dental

Contact Information for Business Card

Needs Names, logo, locations- professional and artsy!

Colors
0555a3
0592cd
34a7d7
3277b5
85cae6
85acd3
cee9f5
ecf7fb

Requirements
Must have
• our names:
• Gavin T. Dalton D.M.D.
• Marla P. Vesh D.M.D.
• Diplomate of the National Council of Gum Surgery
• Address locations:
• 462 N. Larkspur Avenue Suite 210B Plantation, FL 33324
• Tel: 954-603-2281 Fax: 954-603-2895
• 5174 Hollins Lane #C-3 Boca Raton, FL 33434
• Tel: 561-327-6018 Fax: 561-327-6092
• 381 Northwest 7th Street #412 Miami FL 33131
• Tel: 786-540-3316 Fax: 786-540-3389
Nice to have
• unique look
Should not have
• doesn't need QR like our current card has.

```html
<!DOCTYPE html>
<html lang="en">
<head>
<meta charset="utf-8">
<title>Dalton &amp; Vesh Periodontics and Implant Solutions — Business Card</title>
<link href="https://fonts.googleapis.com/css2?family=Source+Sans+3:wght@400;600&display=swap" rel="stylesheet">
<style>
  :root {
    --stage: #000000;
    --navy: #223d7c;
    --navy-dark: #1f3a7a;
    --brand-blue: #0555a3;
    --ring-blue: #1b5fb0;
    --silver: #a7a9ac;
    --paper: #f7f7f7;
    --ghost: #d9d9d9;
  }
  * { margin: 0; padding: 0; box-sizing: border-box; }
  html, body {
    width: 1200px; height: 1000px; overflow: hidden;
    background: var(--stage);
    font-family: "Source Sans 3", "Segoe UI", sans-serif;
  }
  .card {
    position: absolute; left: 274px; width: 651px; height: 381px; overflow: hidden;
  }
  /* Front */
  .card--front { top: 98px; background: var(--navy); }
  .front-ring { position: absolute; left: 0; top: 0; }
  .front-brand {
    position: absolute; left: 0; right: 0; top: 138px; text-align: center; color: var(--silver);
  }
  .front-brand .brand-name { font-size: 50px; font-weight: 400; line-height: 1; letter-spacing: 0.5px; }
  .front-brand .brand-tagline { font-size: 22px; font-weight: 400; line-height: 1.2; margin-top: 2px; }
  .front-contact { margin-top: 6px; font-size: 14.5px; font-weight: 600; line-height: 1.5; }
  .front-contact .sep { margin: 0 6px; }

  /* Back */
  .card--back { top: 530px; background: var(--paper); }
  .back-art { position: absolute; left: 0; top: 0; }
  .back-brand {
    position: absolute; left: 30px; top: 27px; display: flex; align-items: center; gap: 12px;
    color: var(--navy-dark); font-weight: 400;
  }
  .back-brand .brand-mark {
    width: 104px; height: 104px; border: 4px solid var(--navy-dark); border-radius: 50%;
  }
  .back-brand .brand-name { font-size: 30px; line-height: 1; }
  .back-brand .brand-tagline { font-size: 13.5px; line-height: 1.3; }
  .doctors {
    position: absolute; right: 30px; top: 35px; text-align: right;
    font-size: 19px; font-weight: 600; line-height: 24px; color: var(--navy-dark);
  }
  .doctors .credential { color: var(--brand-blue); }
  .locations {
    position: absolute; left: 30px; top: 230px;
    font-size: 15px; font-weight: 600; line-height: 18px; color: var(--brand-blue);
  }
  .location + .location { margin-top: 8px; }
  .location .phones { margin-top: 2px; }
</style>
</head>
<body>

<section class="card card--front">
  <svg class="front-ring" width="651" height="381" viewBox="0 0 651 381" aria-hidden="true">
    <circle cx="326" cy="205" r="125" fill="none" stroke="var(--ring-blue)" stroke-width="10" opacity="0.7"/>
  </svg>
  <div class="front-brand">
    <div class="brand-name">DALTON &amp; VESH</div>
    <div class="brand-tagline">Periodontics and Implant Solutions</div>
    <div class="front-contact">
      <div>462 N. Larkspur Avenue Suite 210B Plantation, FL 33324</div>
      <div>Tel: 954-603-2281<span class="sep">|</span>Fax: 954-603-2895</div>
    </div>
  </div>
</section>

<section class="card card--back">
  <svg class="back-art" width="651" height="381" viewBox="0 0 651 381" aria-hidden="true">
    <circle cx="501" cy="260" r="140" fill="none" stroke="var(--ghost)" stroke-width="12"/>
    <polygon points="386,0 651,0 651,14 400,14" fill="var(--navy)"/>
    <polygon points="0,367 377,367 391,381 0,381" fill="var(--navy)"/>
  </svg>

  <div class="back-brand">
    <div class="brand-mark"></div>
    <div class="brand-text">
      <div class="brand-name">DALTON &amp; VESH</div>
      <div class="brand-tagline">Periodontics and Implant Solutions</div>
    </div>
  </div>

  <div class="doctors">
    <div>Gavin T. Dalton <span class="credential">D.M.D.</span></div>
    <div>Marla P. Vesh <span class="credential">D.M.D.</span></div>
  </div>

  <div class="locations">
    <div class="location">
      <div>5174 Hollins Lane #C-3</div>
      <div>Boca Raton, FL 33434</div>
      <div class="phones">Tel: 561-327-6018 Fax: 561-327-6092</div>
    </div>
    <div class="location">
      <div>381 Northwest 7th Street #412</div>
      <div>Miami FL 33131</div>
      <div class="phones">Tel: 786-540-3316 Fax: 786-540-3389</div>
    </div>
  </div>
</section>

</body>
</html>
```